Acupuncture Medspa needs a business card design

I need a business card design that looks professional, has a spa-like quality and can offer a promo on the back. Initial promo is "First session free". The tagline of NeedleNook is: Refresh, Restore, Rejuvenate.

NeedleNook is a membership-based acupuncture medspa that offers acupuncture, cupping, and herbal therapies. Members choose between the "Refresh" membership which is for stress relief, or "Restore" which is for treating health conditions, and lastly "Rejuvenate" which is for natural facial enhancement.

Industry/Entity Type

Health And Wellness

Contact Information for Business Card

Coral Haskins, MAC, L.Ac.
612-555-0193
www.needlenook-example.com

Font styles to use
Serif
Sans Serif

Colors

Designer to choose colors to be used in the design.

Requirements
Must have
• The project must have NeedleNook logo, promo on the back, and contact information
Nice to have
• I would like to see the colors of the logo used.

```html
<!DOCTYPE html>
<html lang="en">
<head>
<meta charset="utf-8">
<title>NeedleNook Business Card</title>
<link rel="stylesheet" href="https://fonts.googleapis.com/css2?family=Montserrat:wght@400;500;600;700&display=swap">
<style>
  :root {
    --teal: #23877d;
    --teal-light: #2a9287;
    --teal-dark: #1f7a70;
    --white: #ffffff;
    --label: #3a3a3a;
    --page: #ffffff;
  }
  html, body {
    margin: 0;
    padding: 0;
    width: 774px;
    height: 1200px;
    overflow: hidden;
    background: var(--page);
    font-family: "Montserrat", Arial, sans-serif;
  }
  .canvas {
    position: relative;
    width: 774px;
    height: 1200px;
  }
  .side-label {
    position: absolute;
    left: 0;
    width: 774px;
    text-align: center;
    font-size: 15px;
    font-weight: 500;
    letter-spacing: 1px;
    color: var(--label);
  }
  .label-front { top: 76px; }
  .label-back { top: 430px; }
  .card {
    position: absolute;
    left: 181px;
    width: 412px;
    height: 234px;
    overflow: hidden;
    background: var(--teal);
  }
  .card-front { top: 103px; }
  .card-back { top: 457px; }
  .texture {
    position: absolute;
    inset: 0;
    background: linear-gradient(135deg, var(--teal-light), var(--teal) 50%, var(--teal-dark));
  }
  .brand-name {
    position: absolute;
    left: 0;
    width: 100%;
    top: 100px;
    text-align: center;
    font-size: 30px;
    font-weight: 600;
    letter-spacing: 1px;
    line-height: 1;
    color: var(--white);
  }
  .front-web {
    position: absolute;
    left: 0;
    width: 100%;
    top: 197px;
    text-align: center;
    font-size: 8px;
    letter-spacing: 1.5px;
    color: var(--white);
  }
  .card-back svg { display: block; }
</style>
</head>
<body>
<main class="canvas">
  <div class="side-label label-front">FRONT</div>
  <section class="card card-front">
    <div class="texture" role="img" aria-label="Subtle repeating botanical pattern in teal tones"></div>
    <div class="brand-name">NEEDLENOOK</div>
    <div class="front-web">www.needlenook-example.com</div>
  </section>

  <div class="side-label label-back">BACK</div>
  <section class="card card-back">
    <svg width="412" height="234" viewBox="0 0 412 234">
      <circle class="ring" cx="84" cy="117" r="128" fill="none" stroke="#ffffff" stroke-width="2"/>
      <circle class="disc" cx="80" cy="117" r="122" fill="#ffffff"/>
      <text class="back-brand" x="98" y="124" text-anchor="middle" font-family="Montserrat, Arial, sans-serif" font-size="21" font-weight="600" fill="#23877d" letter-spacing="0.5">NEEDLENOOK</text>
      <text class="promo" x="218" y="122" font-family="Montserrat, Arial, sans-serif" font-size="16" font-weight="500" fill="#ffffff" letter-spacing="0.6">FIRST SESSION FREE</text>
      <text class="contact-name" x="218" y="182" font-family="Montserrat, Arial, sans-serif" font-size="8" font-weight="500" fill="#ffffff" letter-spacing="0.8">CORAL HASKINS, MAC, L.AC.</text>
      <text class="contact-phone" x="218" y="195" font-family="Montserrat, Arial, sans-serif" font-size="8" fill="#ffffff" letter-spacing="0.8">612-555-0193</text>
    </svg>
  </section>
</main>
</body>
</html>
```